Website Development for quillmarsh.com.au

Build a new Wordpress/Responsive website for quillmarsh.com.au

Target Market(s)

Compliance Managers, Risk Managers, Information Security and Cyber Security Professionals, Chief Data/Digital Officers, Chief Operating/Financial Officers, Business Continuity Professionals, Disaster Recovery Planners, Small Business Owners, Local/Federal Government entities

Industry/Entity Type

Data Service

Coding

Coded - Design and coding required

Number of Pages Required

5+ page

Font styles to use
Sans Serif

Colors

Designer to choose colors to be used in the design.

Requirements
Must have
• 1. Site Structure: Home Page plus the following chapter-pages for a) Services b) About c) Resources d) Blog e) Contact Us
• 2. Prefer site to built on wordpress and we can purchase a theme if needed (we currently use The7 for other sites)
• 3. Blog needs to be wordpress based
• 4. We will host the site ourselves on our own servers
• 5. Responsive Design
Nice to have
• 1. Livechat capability/interface
• 2. Capability for marketing automation integration (such as hubspot, marketo, infusionsoft etc)
• 3. Capability for CRM integration (Salesforce)

```html
<!DOCTYPE html>
<html lang="en">
<head>
<meta charset="utf-8">
<title>Quillmarsh – Home</title>
<link rel="stylesheet" href="https://fonts.googleapis.com/css2?family=Montserrat:wght@400;500;600;700&family=Open+Sans:wght@400;600;700&display=swap">
<style>
:root{
  --red:#e0101f;
  --red-dark:#b50c18;
  --navy:#0c1a33;
  --navy-deep:#070f1f;
  --ink:#1c1c1c;
  --body:#6a6a6a;
  --ghost:#e9e9e9;
  --band:#f2f2f2;
  --white:#ffffff;
}
*{box-sizing:border-box;margin:0;padding:0}
html,body{width:1200px;height:4986px;overflow:hidden}
body{position:relative;font-family:"Open Sans",Arial,sans-serif;color:var(--ink);background:var(--white)}
.abs{position:absolute}

/* hero */
.hero{left:0;top:0;width:1200px;height:720px;background:radial-gradient(ellipse at 55% 35%,#253a63 0%,#13254a 40%,var(--navy-deep) 100%)}
.brand{left:100px;top:48px;display:flex;align-items:center;gap:14px;color:var(--white);font-family:"Montserrat",Arial,sans-serif;font-weight:700;font-size:32px;letter-spacing:1px}
.brand-dot{width:38px;height:38px;border-radius:50%;background:var(--red)}
.nav{left:465px;top:72px;display:flex;gap:30px;font-family:"Montserrat",Arial,sans-serif;font-size:14px;font-weight:500;color:var(--white);letter-spacing:.5px}
.nav .active{color:var(--red)}
.search{left:1070px;top:70px}
.hero-title{left:0;width:1200px;top:196px;text-align:center;color:var(--white);font-family:"Montserrat",Arial,sans-serif;font-weight:600;font-size:72px;letter-spacing:2px}
.hero-sub{left:0;width:1200px;top:302px;text-align:center;color:var(--white);font-size:24px;font-weight:600}
.btn-outline{left:492px;top:375px;width:216px;height:56px;border:2px solid var(--white);border-radius:28px;color:var(--white);font-family:"Montserrat",Arial,sans-serif;font-weight:700;font-size:15px;display:flex;align-items:center;justify-content:center;letter-spacing:.5px}
.live-chat{left:1154px;top:240px;width:46px;height:160px;background:var(--red);color:var(--white);font-family:"Montserrat",Arial,sans-serif;font-weight:700;font-size:14px;writing-mode:vertical-rl;display:flex;align-items:center;justify-content:center;letter-spacing:1px}

/* section headings */
.section-title{left:0;width:1200px;text-align:center}
.section-title .ghost{position:absolute;left:0;width:1200px;top:-40px;font-family:"Montserrat",Arial,sans-serif;font-weight:700;font-size:108px;color:var(--ghost);letter-spacing:4px}
.section-title .main{position:relative;font-family:"Montserrat",Arial,sans-serif;font-weight:700;font-size:54px;letter-spacing:2px;color:var(--ink)}

/* services */
.service{width:300px;text-align:center}
.service svg{display:block;margin:0 auto 16px}
.service h3{font-family:"Montserrat",Arial,sans-serif;font-weight:500;font-size:23px;line-height:33px;color:var(--ink);margin-bottom:16px}
.service p{font-size:13px;line-height:22px;color:var(--body)}
.btn-red{height:54px;border-radius:27px;background:var(--red);color:var(--white);font-family:"Montserrat",Arial,sans-serif;font-weight:700;font-size:15px;display:flex;align-items:center;justify-content:center;letter-spacing:.5px}

/* about */
.about{left:0;top:1868px;width:1200px;height:642px;background:var(--band)}
.about-ghost{left:110px;top:1935px;font-family:"Montserrat",Arial,sans-serif;font-weight:700;font-size:104px;color:#e2e2e2;letter-spacing:4px}
.about-title{left:112px;top:1975px;font-family:"Montserrat",Arial,sans-serif;font-weight:700;font-size:54px;letter-spacing:2px}
.about-text{left:112px;top:2080px;width:530px;font-size:13.5px;line-height:24px;color:var(--body)}
.about-text p+p{margin-top:16px}
.about-visual{left:690px;top:1880px;width:490px;height:610px;background:linear-gradient(150deg,#3a4a66 0%,#1a2740 55%,#0e1728 100%)}

/* resources */
.res-card{top:2809px;height:332px;overflow:hidden}
.res-photo{width:100%;height:100%}
.res-caption{left:0;right:0;bottom:22px;text-align:center;color:var(--white)}
.res-caption h4{font-family:"Montserrat",Arial,sans-serif;font-weight:600;font-size:24px;margin-bottom:10px}
.meta{font-size:12px;display:flex;gap:16px;justify-content:center;align-items:center}
.meta span{display:flex;align-items:center;gap:5px}
.res-featured{left:409px;width:382px;background:var(--red);color:var(--white);text-align:center;padding:50px 24px 0}
.res-featured h4{font-family:"Montserrat",Arial,sans-serif;font-weight:600;font-size:22px;white-space:nowrap;margin-bottom:12px}
.res-featured p{font-size:13px;line-height:22px;margin-top:18px;padding:0 16px}
.res-featured .more{font-family:"Montserrat",Arial,sans-serif;font-weight:700;font-size:13px;margin-top:22px}
.arrow{top:2940px}

/* blog */
.blog-title{font-family:"Montserrat",Arial,sans-serif;font-weight:600;color:var(--ink)}
.blog-meta{font-size:12px;color:var(--body);display:flex;gap:16px}
.blog-meta span{display:flex;align-items:center;gap:5px}
.blog-text{font-size:13px;line-height:22px;color:var(--body)}
.read-more{font-family:"Montserrat",Arial,sans-serif;font-weight:700;font-size:12.5px;color:var(--red)}

/* contact */
.contact{left:0;top:4170px;width:1200px;height:816px;background:radial-gradient(ellipse at 40% 40%,#1d2d4a 0%,#101c32 45%,var(--navy-deep) 100%)}
.contact-ghost{left:0;width:1200px;top:4385px;text-align:center;font-family:"Montserrat",Arial,sans-serif;font-weight:700;font-size:104px;color:rgba(255,255,255,.07);letter-spacing:4px}
.contact-title{left:0;width:1200px;top:4405px;text-align:center;font-family:"Montserrat",Arial,sans-serif;font-weight:700;font-size:54px;color:var(--white);letter-spacing:2px}
.col-label{font-family:"Montserrat",Arial,sans-serif;font-weight:500;font-size:24px;color:var(--white)}
.field{height:32px;background:var(--white);font-size:11px;color:#777;padding:0 10px;display:flex;align-items:center}
.textarea{align-items:flex-start;padding-top:8px}
.info-row{left:804px;display:flex;align-items:center;gap:22px;color:var(--white);font-size:13.5px;line-height:21px}
.info-icon{width:36px;height:36px;border-radius:50%;border:2px solid var(--red);display:flex;align-items:center;justify-content:center;flex:none}
.footer-line{left:110px;top:4898px;width:980px;height:1px;background:rgba(255,255,255,.18)}
.copyright{left:110px;top:4928px;font-size:13px;color:#c8ccd4}
.socials{left:908px;top:4918px;display:flex;gap:14px}
.socials span{width:34px;height:34px;border-radius:50%;border:1.5px solid var(--white)}
</style>
</head>
<body>

<!-- HERO -->
<div class="abs hero" role="img" aria-label="Dark blue background of glowing data network lines"></div>
<svg class="abs" style="left:0;top:0" width="1200" height="760" aria-hidden="true">
  <path d="M0,592 C300,560 440,690 600,690 C760,690 900,560 1200,592 L1200,760 L0,760Z" fill="#fff"/>
  <circle cx="600" cy="690" r="52" fill="#fff"/>
  <circle cx="600" cy="690" r="30" fill="none" stroke="#e0101f" stroke-width="5"/>
</svg>
<div class="abs brand"><span class="brand-dot"></span>QUILLMARSH</div>
<nav class="abs nav"><span class="active">HOME</span><span>SERVICES</span><span>ABOUT</span><span>RESOURCES</span><span>BLOG</span><span>CONTACT US</span></nav>
<svg class="abs search" width="18" height="18" viewBox="0 0 18 18" aria-hidden="true"><circle cx="7.5" cy="7.5" r="5.5" fill="none" stroke="#fff" stroke-width="2"/><path d="M11.5 11.5L16 16" stroke="#fff" stroke-width="2.2" stroke-linecap="round"/></svg>
<h1 class="abs hero-title">QUILLMARSH</h1>
<p class="abs hero-sub">Nemo enim ipsam voluptatem quia voluptas sit asper</p>
<div class="abs btn-outline">GET MORE INFO</div>
<div class="abs live-chat">LIVE CHAT</div>

<!-- SERVICES -->
<div class="abs section-title" style="top:842px"><div class="ghost">SERVICES</div><h2 class="main">SERVICES</h2></div>

<div class="abs service" style="left:93px;top:985px">
  <svg width="90" height="90" viewBox="0 0 90 90" fill="none" stroke="#e0101f" stroke-width="2.5"><path d="M45 8L76 20V44C76 62 62 76 45 82C28 76 14 62 14 44V20Z"/><path d="M32 45L42 55L60 35"/></svg>
  <h3>Compliance<br>Management</h3>
  <p>Ut enim ad minima veniam, quis nostrum exercitationem ullam corporis suscipit laboriosam commodi conse</p>
</div>
<div class="abs service" style="left:450px;top:985px">
  <svg width="90" height="90" viewBox="0 0 90 90" fill="none" stroke="#e0101f" stroke-width="2.5"><circle cx="45" cy="30" r="14"/><path d="M45 44V58M45 58L25 76M45 58L65 76M45 58V80"/><circle cx="22" cy="78" r="5"/><circle cx="68" cy="78" r="5"/><path d="M45 22V30L51 34"/></svg>
  <h3>Risk<br>Management</h3>
  <p>Ut enim ad minima veniam, quis nostrum exercitationem ullam corporis suscipit laboriosam commodi conse</p>
</div>
<div class="abs service" style="left:804px;top:985px">
  <svg width="90" height="90" viewBox="0 0 90 90" fill="none" stroke="#e0101f" stroke-width="2.5"><path d="M22 10H52L68 26V80H22Z"/><path d="M52 10V26H68"/><rect x="36" y="48" width="22" height="18" rx="2"/><path d="M40 48V42A7 7 0 0 1 54 42V48"/></svg>
  <h3>Information<br>Security</h3>
  <p>Ut enim ad minima veniam, quis nostrum exercitationem ullam corporis suscipit laboriosam commodi conse</p>
</div>
<div class="abs service" style="left:93px;top:1318px">
  <svg width="90" height="90" viewBox="0 0 90 90" fill="none" stroke="#e0101f" stroke-width="2.5"><ellipse cx="45" cy="46" rx="14" ry="20"/><path d="M45 26V66M31 40H18M31 52H18M59 40H72M59 52H72M36 28L28 18M54 28L62 18M36 64L28 74M54 64L62 74"/></svg>
  <h3>Cyber<br>Security</h3>
  <p>Ut enim ad minima veniam, quis nostrum exercitationem ullam corporis suscipit laboriosam commodi conse</p>
</div>
<div class="abs service" style="left:450px;top:1318px">
  <svg width="90" height="90" viewBox="0 0 90 90" fill="none" stroke="#e0101f" stroke-width="2.5"><ellipse cx="40" cy="20" rx="24" ry="8"/><path d="M16 20V64C16 68 27 72 40 72M64 20V40"/><path d="M16 35C16 39 27 43 40 43S64 39 64 35M16 50C16 54 27 58 40 58"/><path d="M64 46L80 52V64C80 72 72 78 64 80C56 78 48 72 48 64V52Z"/></svg>
  <h3>Data<br>Security</h3>
  <p>Ut enim ad minima veniam, quis nostrum exercitationem ullam corporis suscipit laboriosam commodi conse</p>
</div>
<div class="abs service" style="left:804px;top:1318px">
  <svg width="90" height="90" viewBox="0 0 90 90" fill="none" stroke="#e0101f" stroke-width="2.5"><path d="M26 50A18 18 0 0 1 34 22A22 22 0 0 1 72 32A14 14 0 0 1 68 50Z"/><path d="M30 58A18 18 0 0 0 62 64M62 64V56M62 64H54"/><rect x="14" y="68" width="62" height="12" rx="2"/></svg>
  <h3>Disaster<br>Recovery</h3>
  <p>Ut enim ad minima veniam, quis nostrum exercitationem ullam corporis suscipit laboriosam commodi conse</p>
</div>

<div class="abs btn-red" style="left:517px;top:1662px;width:166px">VIEW MORE</div>

<!-- ABOUT -->
<div class="abs about"></div>
<div class="abs about-ghost">ABOUT</div>
<h2 class="abs about-title">ABOUT</h2>
<div class="abs about-text">
  <p>At vero eos et accusamus et iusto odio dignissimos ducimus qui blanditiis praesentium voluptatum deleniti atque corrupti quos dolores et quas molestias excepturi sint occaecati cupiditate.</p>
  <p>Similique sunt in culpa qui officia deserunt mollitia animi, id est laborum et dolorum fuga. Et harum quidem rerum facilis est et expedita distinctio. Nam libero tempore, cum soluta nobis est eligendi optio cumque nihil impedit quo minus id quod maxime placeat facere possimus.</p>
</div>
<div class="abs btn-red" style="left:112px;top:2360px;width:164px">READ MORE</div>
<div class="abs about-visual" role="img" aria-label="Illustration of a hand touching digital security icons on a dark blue screen"></div>

<!-- RESOURCES -->
<div class="abs section-title" style="top:2655px"><div class="ghost">RESOURCES</div><h2 class="main">RESOURCES</h2></div>

<div class="abs res-card" style="left:0;width:385px">
  <div class="res-photo" role="img" aria-label="Photo of people working at computer screens" style="background:linear-gradient(160deg,#4d5d70,#1e2a38)"></div>
  <div class="abs res-caption"><h4>Finibus Bonoret Malorum</h4>
    <div class="meta"><span><svg width="11" height="11" viewBox="0 0 11 11"><rect x="1" y="2" width="9" height="8" fill="none" stroke="#e0101f" stroke-width="1.4"/><path d="M1 4.5H10" stroke="#e0101f"/></svg>15/02/2018</span><span><svg width="10" height="11" viewBox="0 0 10 11"><circle cx="5" cy="3" r="2.5" fill="#e0101f"/><path d="M0 11A5 5 0 0 1 10 11Z" fill="#e0101f"/></svg>John</span></div></div>
</div>
<div class="abs res-card res-featured">
  <h4>Finibus Bonoret Malorum</h4>
  <div class="meta"><span><svg width="11" height="11" viewBox="0 0 11 11"><rect x="1" y="2" width="9" height="8" fill="none" stroke="#fff" stroke-width="1.4"/><path d="M1 4.5H10" stroke="#fff"/></svg>15/02/2018</span><span><svg width="10" height="11" viewBox="0 0 10 11"><circle cx="5" cy="3" r="2.5" fill="#fff"/><path d="M0 11A5 5 0 0 1 10 11Z" fill="#fff"/></svg>John</span></div>
  <p>Nam libero tempore, cum soluta nobis est eligendi optio cumque nihil impedit quo minus id quod maxime placeat facere possi.</p>
  <div class="more">READ MORE</div>
</div>
<div class="abs res-card" style="left:818px;width:382px">
  <div class="res-photo" role="img" aria-label="Photo of a person in a suit using a laptop" style="background:linear-gradient(160deg,#8a97a8,#2d3a4c)"></div>
  <div class="abs res-caption"><h4>Finibus Bonoret Malorum</h4>
    <div class="meta"><span><svg width="11" height="11" viewBox="0 0 11 11"><rect x="1" y="2" width="9" height="8" fill="none" stroke="#e0101f" stroke-width="1.4"/><path d="M1 4.5H10" stroke="#e0101f"/></svg>15/02/2018</span><span><svg width="10" height="11" viewBox="0 0 10 11"><circle cx="5" cy="3" r="2.5" fill="#e0101f"/><path d="M0 11A5 5 0 0 1 10 11Z" fill="#e0101f"/></svg>John</span></div></div>
</div>
<svg class="abs arrow" style="left:36px" width="24" height="44" viewBox="0 0 24 44" aria-hidden="true"><path d="M20 4L4 22L20 40" fill="none" stroke="#fff" stroke-width="4"/></svg>
<svg class="abs arrow" style="left:1130px" width="24" height="44" viewBox="0 0 24 44" aria-hidden="true"><path d="M4 4L20 22L4 40" fill="none" stroke="#fff" stroke-width="4"/></svg>

<!-- BLOG -->
<div class="abs section-title" style="top:3288px"><div class="ghost">BLOG</div><h2 class="main">BLOG</h2></div>

<div class="abs" role="img" aria-label="Photo of a hand holding a phone above a laptop keyboard" style="left:110px;top:3440px;width:452px;height:283px;background:linear-gradient(150deg,#e4e4e4,#8a8a8a)"></div>
<h3 class="abs blog-title" style="left:110px;top:3755px;font-size:22px">Finibus Bonoret et Malorum</h3>
<div class="abs blog-meta" style="left:110px;top:3800px"><span><svg width="11" height="11" viewBox="0 0 11 11"><rect x="1" y="2" width="9" height="8" fill="none" stroke="#e0101f" stroke-width="1.4"/><path d="M1 4.5H10" stroke="#e0101f"/></svg>17/01/2019</span><span><svg width="10" height="11" viewBox="0 0 10 11"><circle cx="5" cy="3" r="2.5" fill="#e0101f"/><path d="M0 11A5 5 0 0 1 10 11Z" fill="#e0101f"/></svg>John Doe</span></div>
<p class="abs blog-text" style="left:110px;top:3838px;width:452px">Nam libero tempore, cum soluta nobis est eligendi optio cumque nihil impedit quo minus id quod maxime placeat fac.</p>
<div class="abs read-more" style="left:110px;top:3918px">READ MORE</div>

<div class="abs" role="img" aria-label="Photo of a laptop with glowing light" style="left:592px;top:3444px;width:232px;height:212px;background:linear-gradient(150deg,#d5a6c4,#5b3c6e)"></div>
<h3 class="abs blog-title" style="left:851px;top:3440px;font-size:17px">Finibus Bonoruet Malorm</h3>
<div class="abs blog-meta" style="left:851px;top:3475px"><span><svg width="11" height="11" viewBox="0 0 11 11"><rect x="1" y="2" width="9" height="8" fill="none" stroke="#e0101f" stroke-width="1.4"/><path d="M1 4.5H10" stroke="#e0101f"/></svg>17/01/2019</span><span><svg width="10" height="11" viewBox="0 0 10 11"><circle cx="5" cy="3" r="2.5" fill="#e0101f"/><path d="M0 11A5 5 0 0 1 10 11Z" fill="#e0101f"/></svg>John Doe</span></div>
<p class="abs blog-text" style="left:851px;top:3508px;width:250px">Nam libero tempore, cum soluta nobis est eligendi optio cumque nihil impedit quo minus id quod maxime placeat facere.</p>
<div class="abs read-more" style="left:851px;top:3640px">READ MORE</div>

<div class="abs" role="img" aria-label="Photo of a person working at a desk with monitors" style="left:592px;top:3710px;width:232px;height:222px;background:linear-gradient(150deg,#5c6a78,#1d2630)"></div>
<h3 class="abs blog-title" style="left:851px;top:3706px;font-size:17px">Finibus Bonoruet Malorm</h3>
<div class="abs blog-meta" style="left:851px;top:3741px"><span><svg width="11" height="11" viewBox="0 0 11 11"><rect x="1" y="2" width="9" height="8" fill="none" stroke="#e0101f" stroke-width="1.4"/><path d="M1 4.5H10" stroke="#e0101f"/></svg>17/01/2019</span><span><svg width="10" height="11" viewBox="0 0 10 11"><circle cx="5" cy="3" r="2.5" fill="#e0101f"/><path d="M0 11A5 5 0 0 1 10 11Z" fill="#e0101f"/></svg>John Doe</span></div>
<p class="abs blog-text" style="left:851px;top:3774px;width:250px">Nam libero tempore, cum soluta nobis est eligendi optio cumque nihil impedit quo minus id quod maxime placeat facere.</p>
<div class="abs read-more" style="left:851px;top:3906px">READ MORE</div>

<div class="abs btn-red" style="left:517px;top:4008px;width:166px">VIEW MORE</div>

<!-- CONTACT -->
<div class="abs contact" role="img" aria-label="Dark blue background photo of a city at night"></div>
<svg class="abs" style="left:0;top:4160px" width="1200" height="160" aria-hidden="true">
  <path d="M0,0 H1200 V50 C900,60 760,130 600,130 C440,130 300,60 0,50Z" fill="#fff"/>
  <circle cx="600" cy="92" r="50" fill="#fff"/>
  <circle cx="600" cy="92" r="30" fill="none" stroke="#e0101f" stroke-width="5"/>
</svg>
<div class="abs contact-ghost">CONTACT</div>
<h2 class="abs contact-title">CONTACT</h2>

<div class="abs col-label" style="left:110px;top:4530px">Contact form</div>
<div class="abs field" style="left:110px;top:4604px;width:312px">First Name</div>
<div class="abs field" style="left:435px;top:4604px;width:306px">Last Name</div>
<div class="abs field" style="left:110px;top:4650px;width:312px">Email</div>
<div class="abs field" style="left:435px;top:4650px;width:306px">Phone Number</div>
<div class="abs field textarea" style="left:110px;top:4696px;width:631px;height:84px">Comments</div>
<div class="abs btn-red" style="left:632px;top:4800px;width:109px;height:42px;border-radius:21px;font-size:13px">SUBMIT</div>

<div class="abs col-label" style="left:804px;top:4530px">Contact Information</div>
<div class="abs info-row" style="top:4600px">
  <span class="info-icon"><svg width="14" height="18" viewBox="0 0 14 18"><path d="M7 17C7 17 1 10 1 6.5A6 6 0 0 1 13 6.5C13 10 7 17 7 17Z" fill="none" stroke="#e0101f" stroke-width="1.8"/><circle cx="7" cy="6.5" r="2" fill="#e0101f"/></svg></span>
  <span>Temporibus autem quibusd<br>San Francisco Bay Area</span>
</div>
<div class="abs info-row" style="top:4686px">
  <span class="info-icon"><svg width="16" height="16" viewBox="0 0 16 16"><path d="M3 1L6 4L4.5 6.5C5.5 8.5 7.5 10.5 9.5 11.5L12 10L15 13L13 15C7 15 1 9 1 3Z" fill="#e0101f"/></svg></span>
  <span>1 888 888 888</span>
</div>
<div class="abs info-row" style="top:4758px">
  <span class="info-icon"><svg width="16" height="12" viewBox="0 0 16 12"><rect x="1" y="1" width="14" height="10" fill="none" stroke="#e0101f" stroke-width="1.6"/><path d="M1 1L8 7L15 1" fill="none" stroke="#e0101f" stroke-width="1.6"/></svg></span>
  <span>info@quillmarsh.com.au</span>
</div>

<div class="abs footer-line"></div>
<p class="abs copyright">Copyright © 2019, Quillmarsh. All rights reserved.</p>
<div class="abs socials" aria-label="Social links"><span></span><span></span><span></span><span></span></div>

</body>
</html>
```